Briefing for Nexoria Desk Business Card Design:

Objective:
To design business cards that represent the vision and mission of Nexoria Desk, a company that aims to create the best remote work experience for people and companies, with a focus on simplicity and ease of use.

Design Elements:

Color Scheme: Blue and White
Font: Modern and Clean
Logo: The Nexoria Desk logo should be prominently displayed on the card.
Vision Statement: "Helping businesses create workplaces where people love to work" should be included on the card.
Mission Statement: "Create the best remote work experience for people and companies" should also be included.
Key Focus: The card should emphasize Nexoria Desk's focus on simplicity and ease of use in its cloud solutions.
Design Concept:
The design of the business card should be simple yet professional. The Nexoria Desk logo should be the focal point of the card, and the blue and white color scheme should be used to create a clean and modern feel that reinforces the idea of simplicity and ease of use. Blue represents trust, professionalism, and reliability, while white represents purity, simplicity, and clarity. The card should feature the vision and mission of the company, with each statement being given equal importance. The font used should be modern and clean, with legibility being a top priority. A tagline could be included that emphasizes the company's focus on simplicity and ease of use, such as "Simplicity at its best" or "Streamlined cloud solutions."

Final Thoughts:
The design of the business card should represent Nexoria Desk's vision and mission while also conveying the message that the company is the choice for those who value simplicity and ease of use in their cloud solutions. The final product should leave a lasting impression on anyone who receives it, and it should convey the professionalism and expertise of Nexoria Desk in helping businesses create workplaces where people love to work. The blue and white color scheme can be a great choice for the Nexoria Desk business card design, and it can help to create a professional and memorable impression on clients and partners while emphasizing the company's focus on simplicity and ease of use.

Target Market(s)

Companies that employ remote workers that work on computers

Industry/Entity Type

SaaS

Contact Information for Business Card

Website: www.nexoriadesk.example, phone, email, whatsApp, LinkedIn,

Font styles to use
Other font styles liked:
• Main Fonts: Poppins Light, Poppins Medium, Poppins Bold Alternative Fonts (for Sub Headers) Cairo Light, Cairo Regular, Cairo Bold

Colors
0054AA
0677BA
7BADD7
CADEEF
E8F1F8

Requirements
Must have
Nice to have
• Most of of our competitors treat you like a number, we give a sh!t, we take the time to help people get set up and grow. Think of the Zorvan vs Plinthar commercials from the early 2000s

```html
<!DOCTYPE html>
<html lang="en">
<head>
<meta charset="utf-8">
<title>Nexoria Desk Business Card</title>
<link rel="stylesheet" href="https://fonts.googleapis.com/css2?family=Poppins:wght@400;500;600;700&display=swap">
<style>
  :root {
    --bg: #e9e9e9;
    --white: #ffffff;
    --blue-deep: #0054aa;
    --blue-card: #0c6d9f;
    --blue-mid: #0677ba;
    --blue-bright: #1a9ddb;
    --blue-soft: #7badd7;
    --text-grey: #4a4a4a;
    --rule: #9a9a9a;
  }
  * { margin: 0; padding: 0; box-sizing: border-box; }
  html, body { width: 1200px; height: 802px; overflow: hidden; }
  body {
    background: var(--bg);
    font-family: "Poppins", sans-serif;
    position: relative;
  }
  .card {
    position: absolute;
    top: 252px;
    width: 520px;
    height: 298px;
    box-shadow: 0 10px 28px rgba(0,0,0,0.14);
  }
  .card-front { left: 60px; background: var(--white); }
  .card-back { left: 620px; background: var(--blue-card); }

  .front-brand {
    position: absolute;
    left: 0; top: 0;
    width: 230px; height: 100%;
    display: flex; align-items: center; justify-content: center;
    gap: 10px;
  }
  .brand-dot {
    width: 22px; height: 22px; border-radius: 50%;
    background: var(--blue-mid);
  }
  .brand-name {
    font-weight: 700;
    font-size: 27px;
    letter-spacing: -0.5px;
    color: var(--blue-mid);
  }
  .divider {
    position: absolute;
    left: 236px; top: 72px;
    width: 1px; height: 154px;
    background: var(--rule);
  }
  .front-details {
    position: absolute;
    left: 262px; top: 66px;
  }
  .person-name {
    font-weight: 600;
    font-size: 20px;
    color: var(--blue-bright);
    letter-spacing: 0.2px;
    line-height: 1.1;
  }
  .person-title {
    font-size: 13px;
    color: var(--text-grey);
    margin-bottom: 14px;
  }
  .contact-list { list-style: none; }
  .contact-list li {
    display: flex; align-items: center; gap: 9px;
    font-size: 12.5px;
    color: var(--text-grey);
    line-height: 1.65;
  }
  .contact-icon { width: 13px; height: 13px; flex: none; }

  .back-brand {
    position: absolute;
    right: 70px; top: 0;
    height: 100%;
    display: flex; align-items: center; gap: 12px;
  }
  .back-brand .brand-dot { background: var(--blue-soft); width: 26px; height: 26px; }
  .back-brand .brand-name { color: var(--white); font-size: 32px; }
</style>
</head>
<body>
  <section class="card card-front">
    <div class="front-brand">
      <span class="brand-dot"></span>
      <span class="brand-name">Nexoria Desk</span>
    </div>
    <div class="divider"></div>
    <div class="front-details">
      <p class="person-name">MARLOW FENWICK</p>
      <p class="person-title">Manager</p>
      <ul class="contact-list">
        <li><svg class="contact-icon" viewBox="0 0 14 14"><circle cx="7" cy="7" r="6.5" fill="#1a9ddb"/></svg>555-014-2100</li>
        <li><svg class="contact-icon" viewBox="0 0 14 14"><rect x="0.5" y="0.5" width="13" height="13" rx="2" fill="#1a9ddb"/></svg># nexoriadesk</li>
        <li><svg class="contact-icon" viewBox="0 0 14 14"><path d="M3 1.5 L5.5 1.5 L6.3 4.3 L4.8 5.5 Q6 8.3 8.5 9.3 L9.7 7.8 L12.5 8.6 L12.5 11 Q12 12.5 10.5 12.5 Q2 11.5 1.5 3 Q1.5 1.7 3 1.5 Z" fill="#1a9ddb"/></svg>555-014-2100</li>
        <li><svg class="contact-icon" viewBox="0 0 14 14"><rect x="0.5" y="2.5" width="13" height="9" rx="1" fill="#1a9ddb"/><path d="M1 3.2 L7 8 L13 3.2" fill="none" stroke="#fff" stroke-width="1.2"/></svg>marlow@nexoriadesk.example</li>
        <li><svg class="contact-icon" viewBox="0 0 14 14"><circle cx="7" cy="7" r="6" fill="none" stroke="#1a9ddb" stroke-width="1.4"/><ellipse cx="7" cy="7" rx="2.6" ry="6" fill="none" stroke="#1a9ddb" stroke-width="1.1"/><line x1="1" y1="7" x2="13" y2="7" stroke="#1a9ddb" stroke-width="1.1"/></svg>www.nexoriadesk.example</li>
      </ul>
    </div>
  </section>

  <section class="card card-back">
    <div class="back-brand">
      <span class="brand-dot"></span>
      <span class="brand-name">Nexoria Desk</span>
    </div>
  </section>
</body>
</html>
```